Wedding design templates - fresh

We require 3 different wedding designs. I have attached the watercolour images for the graphic designer to use on each template. I want to be able to easily change the name and location of the invitation when needed and be able to freely use whatever font is used, so that the invite becomes our template. I want something fresh with a modern layout but on a white background. The use of coloured fonts are okay to suit the images provided. The size of the card stock is A5 (half of an A4) please consider bleeds etc for printing.

Target Market(s)

Bridal market - young couples

Industry/Entity Type

Wedding

Font styles to use
Serif
Sans Serif
Script

Requirements
Must have
• Be able to use fonts and change details easily. common colours that can easily fit in with a brides colour scheme. must have all details for wedding invites ie church name address etc can be any church or reception place in sydney
Nice to have
• i have uploaded some example images as to style i am looking for.
• I want to be able to run a theme with these images eg. rsvp cards, place cards etc

```html
<!DOCTYPE html>
<html lang="en">
<head>
<meta charset="UTF-8">
<title>Clara &amp; Jonas – Wedding Invitation</title>
<link href="https://fonts.googleapis.com/css2?family=Dancing+Script:wght@600&family=Arimo:wght@400&display=swap" rel="stylesheet">
<style>
  :root {
    --backdrop: #2a2a2a;
    --card: #ffffff;
    --teal: #4e97a8;
    --ink: #4c575e;
    --gold: #c49a62;
    --gold-soft: #ead7bd;
    --leaf: #9dbfa4;
    --leaf-deep: #6f8f7a;
    --blush: #f4b7a5;
    --sky: #a9d0de;
    --cream: #f3efe4;
  }
  * { margin: 0; padding: 0; box-sizing: border-box; }
  html, body { width: 1200px; height: 1000px; overflow: hidden; background: var(--backdrop); }
  .canvas { position: relative; width: 1200px; height: 1000px; background: var(--backdrop); }
  .invitation {
    position: absolute; left: 319px; top: 56px; width: 622px; height: 885px;
    background: var(--card);
  }
  .invitation-art { position: absolute; left: 0; top: 0; width: 622px; height: 885px; }
  .invitation-text {
    position: absolute; left: 0; width: 622px; text-align: center;
    font-family: "Arimo", Arial, sans-serif; color: var(--ink);
  }
  .couple-names {
    top: 282px; font-family: "Dancing Script", cursive; font-weight: 600;
    font-size: 66px; line-height: 80px; color: var(--teal); left: 6px;
  }
  .invite-lead { top: 387px; font-size: 19px; line-height: 24px; left: -7px; }
  .guest-line {
    position: absolute; left: 113px; top: 451px; width: 398px;
    border-top: 2px dotted var(--ink);
  }
  .event-details { top: 457px; font-size: 19px; line-height: 23.6px; left: 3px; }
</style>
</head>
<body>
<div class="canvas">
  <div class="invitation">
    <svg class="invitation-art" viewBox="0 0 622 885" xmlns="http://www.w3.org/2000/svg">
      <defs>
        <radialGradient id="bloom-top" cx="45%" cy="45%" r="60%">
          <stop offset="0%" stop-color="#cfe2e4"/>
          <stop offset="45%" stop-color="#f3d2c6"/>
          <stop offset="100%" stop-color="#b8cdb9"/>
        </radialGradient>
        <radialGradient id="bloom-bottom" cx="55%" cy="50%" r="60%">
          <stop offset="0%" stop-color="#f6c6b6"/>
          <stop offset="50%" stop-color="#dbe7dc"/>
          <stop offset="100%" stop-color="#aac4ae"/>
        </radialGradient>
      </defs>

      <!-- oval frame -->
      <g class="oval-frame">
        <ellipse cx="312" cy="434" rx="232" ry="258" fill="none" stroke="var(--gold)" stroke-width="3"/>
        <path role="img" aria-label="Ornamental scroll border around the oval frame"
              fill="var(--gold-soft)" fill-rule="evenodd"
              d="M80,434 a232,258 0 1,0 464,0 a232,258 0 1,0 -464,0 Z
                 M102,434 a210,236 0 1,0 420,0 a210,236 0 1,0 -420,0 Z"/>
        <ellipse cx="312" cy="434" rx="210" ry="236" fill="var(--card)" stroke="var(--gold)" stroke-width="2.5"/>
      </g>

      <!-- watercolour flowers -->
      <path class="floral-top" role="img" aria-label="Watercolour bouquet of blue anemones, white blossoms, peach roses and eucalyptus leaves"
            fill="url(#bloom-top)" opacity="0.95"
            d="M40,95 C70,70 120,80 150,95 C175,60 215,70 240,90 C280,70 330,60 352,45 C380,60 400,100 410,135
               C390,160 340,170 300,180 C250,185 200,200 170,235 C140,270 115,300 100,335
               C80,370 60,380 20,372 C10,340 18,300 35,280 C25,250 30,220 45,200
               C30,170 25,130 40,95 Z"/>
      <path class="floral-bottom" role="img" aria-label="Watercolour bouquet of peach roses, blue anemone, white blossoms, pink berries and green leaves"
            fill="url(#bloom-bottom)" opacity="0.95"
            d="M555,480 C580,500 600,560 598,600 C590,640 600,690 590,730 C595,770 580,820 560,850
               C520,860 470,858 430,845 C390,830 350,810 320,790 C280,790 240,785 225,770
               C260,745 300,725 340,720 C380,700 410,680 440,650 C470,620 500,600 520,560
               C530,530 540,500 555,480 Z"/>
    </svg>

    <div class="invitation-text couple-names">Clara &amp; Jonas</div>
    <div class="invitation-text invite-lead">wish to invite</div>
    <div class="guest-line"></div>
    <div class="invitation-text event-details">
      to join them as they celebrate their marriage<br>
      on Saturday 18th July 2015<br>
      at three in the afternoon<br>
      in ST. BRIDGET'S CHAPEL,<br>
      Sydney.<br>
      Reception to follow.
    </div>
  </div>
</div>
</body>
</html>
```